Brim Physiotherapy Business Card

I need a business card to allow for promotion of my new business as well as to book patients in for appointments.
The business is a pelvic floor health physiotherapy practice specialising in women's and men's continence type care.
It will be a small business offering personal care.
I will be the sole practitioner to start off with.

Target Market(s)

Pregnant and post natal women
Aging women and men
Women with breastfeeding difficulties
Children with bedwetting issues

Industry/Entity Type

Business

Contact Information for Business Card

Previous designs have perhaps been a bit too basic or not really eye catching.

Colors

Designer to choose colors to be used in the design.

Requirements
Must have
• Option to write appointment time and date on the back.
• Attractive and eye catching front.
• Logo somewhere on the card.
Nice to have
• Bright colours.
• Simple design that is easy to print.

```html
<!DOCTYPE html>
<html lang="en">
<head>
<meta charset="utf-8">
<title>Brim Physiotherapy Business Card</title>
<link rel="stylesheet" href="https://fonts.googleapis.com/css2?family=Arimo:wght@400;700&display=swap">
<style>
  :root {
    --backdrop: #3f9795;
    --paper: #f3f2f0;
    --ink: #3a3a3c;
    --purple: #a86cb8;
    --purple-fold: #c59ad1;
    --charcoal-fold: #5a5a5d;
  }
  * { box-sizing: border-box; margin: 0; padding: 0; }
  html, body { width: 1200px; height: 668px; overflow: hidden; }
  body {
    background: var(--backdrop);
    font-family: "Arimo", Arial, sans-serif;
    color: var(--ink);
    position: relative;
  }
  .card {
    position: absolute;
    top: 184px;
    width: 525px;
    height: 300px;
    background: var(--paper);
    overflow: hidden;
  }
  .card--front { left: 50px; }
  .card--back { left: 625px; }
  .card__shapes { position: absolute; inset: 0; width: 100%; height: 100%; }

  .brand { position: absolute; display: flex; align-items: center; gap: 10px; }
  .brand__dot { width: 38px; height: 38px; border-radius: 50%; background: var(--ink); flex: none; }
  .brand__name { font-weight: 700; font-size: 26px; color: var(--ink); white-space: nowrap; }
  .card--front .brand { left: 196px; top: 30px; }
  .card--back .brand { left: 50%; top: 100px; transform: translateX(-50%); }

  .tagline {
    position: absolute; left: 244px; top: 76px;
    font-size: 10px; font-weight: 700; letter-spacing: 0.3px; color: var(--ink);
  }
  .holder__name {
    position: absolute; left: 26px; top: 100px;
    font-size: 21px; font-weight: 700; color: var(--ink);
  }
  .holder__credentials {
    position: absolute; left: 26px; top: 130px; width: 410px;
    font-size: 13px; font-weight: 700; line-height: 1.35; color: var(--purple);
  }
  .contact {
    position: absolute; left: 272px; top: 206px;
    list-style: none; font-size: 14px; font-weight: 700; color: var(--purple);
  }
  .contact li { display: flex; align-items: center; gap: 8px; line-height: 22px; }
  .contact svg { width: 11px; height: 11px; flex: none; fill: var(--ink); }

  .appointment {
    position: absolute; left: 32px; top: 176px; width: 380px;
    font-size: 15px; color: #111;
  }
  .appointment__row { display: flex; align-items: flex-end; gap: 6px; height: 28px; }
  .appointment__line { flex: 1; border-bottom: 1px solid #222; height: 18px; }
  .appointment__blank { border-bottom: 1px solid #222; height: 36px; }
</style>
</head>
<body>

<section class="card card--front" aria-label="Card front">
  <svg class="card__shapes" viewBox="0 0 525 300" aria-hidden="true">
    <rect x="0" y="0" width="525" height="10" fill="var(--purple)"/>
    <polygon points="430,10 525,10 525,200" fill="var(--purple)"/>
    <polygon points="430,10 462,10 498,150" fill="var(--purple-fold)"/>
  </svg>
  <div class="brand"><span class="brand__dot"></span><span class="brand__name">Brim Physiotherapy</span></div>
  <p class="tagline">women's health and pelvic floor physiotherapy</p>
  <h1 class="holder__name">Maya Hollins</h1>
  <p class="holder__credentials">B Physiotherapy, PGradCert Pelvic Floor Physiotherapy (Hons), Cert III in Fitness</p>
  <ul class="contact">
    <li><svg viewBox="0 0 12 12"><path d="M3 0h6a1 1 0 0 1 1 1v10a1 1 0 0 1-1 1H3a1 1 0 0 1-1-1V1a1 1 0 0 1 1-1zm0 2v7h6V2z"/></svg>0412555018</li>
    <li><svg viewBox="0 0 12 12"><path d="M0 2h12v8H0zM1 3l5 4 5-4v-.2H1z"/></svg>www.brimphysio.com.au</li>
    <li><svg viewBox="0 0 12 12"><circle cx="6" cy="6" r="6"/><path d="M1 6h10M6 1v10" stroke="#f3f2f0" stroke-width="1"/></svg>maya@brimphysio.com.au</li>
  </ul>
</section>

<section class="card card--back" aria-label="Card back">
  <svg class="card__shapes" viewBox="0 0 525 300" aria-hidden="true">
    <rect x="0" y="0" width="525" height="8" fill="var(--ink)"/>
    <polygon points="430,8 525,8 525,230" fill="var(--ink)"/>
    <polygon points="430,8 462,8 500,170" fill="var(--charcoal-fold)"/>
    <polygon points="0,40 46,120 0,190" fill="var(--purple)"/>
  </svg>
  <div class="brand"><span class="brand__dot"></span><span class="brand__name">Brim Physiotherapy</span></div>
  <div class="appointment">
    <div class="appointment__row"><span>Appointment Time</span><span class="appointment__line"></span></div>
    <div class="appointment__blank"></div>
    <div class="appointment__blank"></div>
  </div>
</section>

</body>
</html>
```